BUSINESS CARD MIRELLE CAVANOSI

I need a new business card for my personal business.
I am a Naturopath and Nutritionist working doing private consults in the health and wellness arena.
I would like to see designs that are, clean minimalist but colourful.
I like:
White (clean,fresh, minimalist)
pops of one colour ONLY.Choose a colour to run with and keep it simple.
green
light blue
mustard
Bright yellow
Charcoal
The final design should communicate professionalism but also be in touch with nature.
Key Information to include:
MIRELLE CAVANOSI
ABN 48 217 603 915
RQTLBE 327081
Tel 0487 639 142
NATUROPATH | HERBALIST | NUTRITON CONSULTANT
BHSc (Naturopathic Studies) Grad Dip (Naturopathy)
BACK OF CARD : YOUR NEXT APPOINTMENT ..................................
I already have a logo (picture attached)But I would be more than happy to NOT have this included. I am very Open to cards WITHOUT current logo/ ones that weave the colour of my logo but do not use the logo.
I have included pictures attached to give examples of the styles/colors I enjoy.
Updates
I have added a picture of a mortar and pestle - one just like this would be lovely to include in your entry.
TIA

```html
<!DOCTYPE html>
<html lang="en">
<head>
<meta charset="utf-8">
<title>Mirelle Cavanosi Naturopathy – Business Card</title>
<link rel="stylesheet" href="https://fonts.googleapis.com/css2?family=Roboto+Condensed:wght@300;400;700&display=swap">
<style>
  :root {
    --teal: #1bb3a3;
    --teal-deep: #139e90;
    --mint: #bfe9d6;
    --aqua: #7fd6c7;
    --grey-text: #6d6f72;
    --grey-line: #c9ccce;
    --card-white: #fbfcfc;
    --backdrop: #eceeee;
  }
  * { box-sizing: border-box; margin: 0; padding: 0; }
  html, body {
    width: 1200px; height: 1001px; overflow: hidden;
    background: var(--backdrop);
    font-family: "Roboto Condensed", "Arial Narrow", sans-serif;
  }
  .canvas { position: relative; width: 1200px; height: 1001px; }
  .card {
    position: absolute; left: 230px; width: 740px; height: 420px;
    border-radius: 22px; overflow: hidden;
    background: var(--card-white);
    box-shadow: 0 6px 18px rgba(0,0,0,0.12);
  }

  /* Contact side */
  .card--contact { top: 50px; }
  .contact__foliage {
    position: absolute; top: 0; right: 0; width: 330px; height: 200px;
    background: radial-gradient(ellipse at 85% 20%, rgba(127,214,199,0.35), rgba(191,233,214,0.15) 55%, rgba(255,255,255,0) 75%);
  }
  .brand { position: absolute; left: 46px; top: 180px; width: 250px; }
  .brand__name {
    font-size: 29px; font-weight: 400; color: var(--teal); letter-spacing: 0.3px;
    white-space: nowrap;
  }
  .brand__practice {
    margin-top: 4px; font-size: 16px; font-weight: 300; color: var(--grey-text);
    letter-spacing: 7px; white-space: nowrap;
  }
  .contact__divider {
    position: absolute; left: 318px; top: 108px; width: 1px; height: 150px;
    background: var(--grey-line);
  }
  .details {
    position: absolute; left: 338px; top: 112px; font-size: 13px; line-height: 22px;
    color: var(--grey-text); font-weight: 400; white-space: nowrap;
  }
  .details__gap { display: inline-block; width: 34px; }
  .appointment {
    position: absolute; left: 338px; top: 300px; width: 330px;
    font-size: 13px; color: var(--teal);
    padding-bottom: 6px; border-bottom: 1px solid var(--grey-line);
  }

  /* Leaf side */
  .card--leaf { top: 530px; }
  .leaf__field {
    position: absolute; left: 0; top: 0; width: 100%; height: 300px;
    background: linear-gradient(150deg, var(--mint) 0%, var(--aqua) 45%, #a6e2d1 75%, #cdeee0 100%);
  }
  .leaf__band {
    position: absolute; left: 0; bottom: 0; width: 100%; height: 120px;
    background: var(--card-white);
  }
  .leaf__name {
    position: absolute; left: 46px; bottom: 36px;
    font-size: 44px; font-weight: 400; color: var(--teal-deep); letter-spacing: 0.3px;
    white-space: nowrap;
  }
  .leaf__tag { position: absolute; left: 436px; bottom: 44px; white-space: nowrap; }
  .leaf__practice {
    font-size: 23px; font-weight: 300; color: var(--grey-text); letter-spacing: 8px;
  }
  .leaf__services {
    margin-top: 2px; font-size: 14px; font-weight: 400; color: var(--teal);
  }
</style>
</head>
<body>
<main class="canvas">

  <section class="card card--contact">
    <div class="contact__foliage" role="img" aria-label="Faint scattered green leaves"></div>
    <div class="brand">
      <div class="brand__name">MIRELLE CAVANOSI</div>
      <div class="brand__practice">NATUROPATHY</div>
    </div>
    <div class="contact__divider"></div>
    <div class="details">
      <div>ABN 48 217 603 915<span class="details__gap"></span>RQTLBE 327081</div>
      <div>Tel 0487 639 142</div>
      <div>Naturopath | Herbalist | Nutrition consultant</div>
      <div>BHSc (Naturopathic Studies) Grad Dip (Naturopathy)</div>
    </div>
    <div class="appointment">Your Next Appointment</div>
  </section>

  <section class="card card--leaf">
    <div class="leaf__field" role="img" aria-label="Soft pattern of floating teal and mint leaves"></div>
    <div class="leaf__band"></div>
    <div class="leaf__name">MIRELLE CAVANOSI</div>
    <div class="leaf__tag">
      <div class="leaf__practice">NATUROPATHY</div>
      <div class="leaf__services">Naturopath | Herbalist | Nutrition consultant</div>
    </div>
  </section>

</main>
</body>
</html>
```